Oil and Gas Exploration and Production company needs a business card design

We need a business card design using our logo and colors in the logo. We want a mainstream design.

```html
<!DOCTYPE html>
<html lang="en">
<head>
<meta charset="utf-8">
<title>Kestrel Oil &amp; Gas – Business Card</title>
<link rel="stylesheet" href="https://fonts.googleapis.com/css2?family=Arimo:wght@400;700&display=swap">
<style>
  :root {
    --gold: #cdb02f;
    --gold-light: #e2c94a;
    --ink: #1c1c1c;
    --charcoal: #2a2a2a;
    --paper: #ffffff;
    --stage: #e6e4df;
  }
  * { box-sizing: border-box; margin: 0; padding: 0; }
  html, body {
    width: 1200px; height: 1023px; overflow: hidden;
    background: var(--stage);
    font-family: "Arimo", Arial, sans-serif;
  }
  .canvas {
    width: 1200px; height: 1023px;
    display: flex; align-items: center; justify-content: center;
  }
  .card {
    position: relative;
    width: 900px; height: 514px;
    background: var(--paper);
    overflow: hidden;
    box-shadow: 0 10px 30px rgba(0,0,0,.18);
  }
  .top-band {
    position: absolute; left: 0; top: 0; width: 100%; height: 72px;
    background: var(--gold);
    border-bottom: 6px solid var(--ink);
  }
  .tagline {
    position: absolute; left: 30px; top: 20px;
    font-size: 30px; color: #3a3318; letter-spacing: .2px;
    white-space: nowrap;
  }
  .stripes { position: absolute; right: 0; top: 0; }
  .illustration {
    position: absolute; left: 20px; top: 100px; width: 330px; height: 300px;
    background: linear-gradient(160deg, #f4f4f4 0%, #8a8a8a 55%, #222 100%);
  }
  .ground {
    position: absolute; left: 0; bottom: 0; width: 400px; height: 160px;
    background: linear-gradient(180deg, #3a3a3a, var(--charcoal));
  }
  .contact-band {
    position: absolute; right: 0; bottom: 0; width: 500px; height: 190px;
    background: var(--gold);
    border-top: 6px solid var(--ink);
    padding: 36px 0 0 36px;
  }
  .contact-row {
    display: flex; align-items: center; gap: 14px;
    font-size: 18px; color: var(--ink); margin-bottom: 22px;
    white-space: nowrap;
  }
  .contact-icon {
    width: 36px; height: 36px; border-radius: 50%;
    background: var(--paper);
    display: flex; align-items: center; justify-content: center;
    flex-shrink: 0;
  }
  .brand {
    position: absolute; left: 380px; top: 122px;
    display: flex; align-items: center; gap: 18px;
  }
  .brand-dot {
    width: 50px; height: 50px; border-radius: 50%; background: var(--gold);
    flex-shrink: 0;
  }
  .brand-name {
    font-size: 44px; font-weight: 700; color: var(--ink); line-height: 1;
    white-space: nowrap;
  }
  .person { position: absolute; left: 448px; top: 212px; }
  .person-name { font-size: 32px; color: var(--ink); letter-spacing: .5px; white-space: nowrap; }
  .person-title { font-size: 18px; color: var(--ink); margin-top: 10px; white-space: nowrap; }
</style>
</head>
<body>
<main class="canvas">
  <article class="card">
    <header class="top-band">
      <p class="tagline">Exploration and Production company</p>
      <svg class="stripes" width="150" height="72" viewBox="0 0 150 72" aria-hidden="true">
        <polygon points="40,72 62,72 92,0 70,0" fill="#1c1c1c"/>
        <polygon points="74,72 96,72 126,0 104,0" fill="#1c1c1c"/>
        <polygon points="108,72 130,72 150,24 150,0 138,0" fill="#1c1c1c"/>
      </svg>
    </header>

    <div class="illustration" role="img" aria-label="Silhouette of an oil pumpjack and wellhead"></div>
    <div class="ground"></div>

    <div class="brand">
      <span class="brand-dot"></span>
      <span class="brand-name">Kestrel Oil &amp; Gas</span>
    </div>

    <div class="person">
      <p class="person-name">DALE HARTWELL</p>
      <p class="person-title">President for Northcrest Exploration, Inc.</p>
    </div>

    <section class="contact-band">
      <div class="contact-row">
        <span class="contact-icon">
          <svg width="18" height="22" viewBox="0 0 18 22" aria-hidden="true">
            <path d="M9 1a7 7 0 0 0-7 7c0 5 7 13 7 13s7-8 7-13a7 7 0 0 0-7-7z" fill="#1c1c1c"/>
            <circle cx="9" cy="8" r="2.6" fill="#fff"/>
          </svg>
        </span>
        <span>2450 Meadow Bend Dr, Fort Worth, TX 76110</span>
      </div>
      <div class="contact-row">
        <span class="contact-icon">
          <svg width="22" height="22" viewBox="0 0 22 22" aria-hidden="true" fill="none" stroke="#1c1c1c" stroke-width="1.6">
            <circle cx="11" cy="11" r="9"/>
            <ellipse cx="11" cy="11" rx="4" ry="9"/>
            <line x1="2" y1="11" x2="20" y2="11"/>
            <line x1="4" y1="6" x2="18" y2="6"/>
            <line x1="4" y1="16" x2="18" y2="16"/>
          </svg>
        </span>
        <span>https://www.kestreloilgas.com</span>
      </div>
    </section>
  </article>
</main>
</body>
</html>
```